KOR Design

Looking for the website design of an small business,
The company is newly established. The Company Trades with Steel from Asiam Europe to Australia and New Zealand.

In the main Page, we would like to have a video showing the process of how steel is made(or the iron melt, pipe rolled, etc)

We would like to show pictures of the Products we trade and an table with some information about the specifications and Product.

About the company,
Industry is Iron and Steel
The company source and supply various steel and metal products within our international network also manage all aspects of the supply process from point of manufacture to point of delivery. the goal is to create value within the supply chain by building strong supplier, customers and service providers, funding of both customers and suppliers, experienced risk management, efficient document handling.
Main products: LSAW pipe, ERW Pipe, Flat rolled Products (such is Steel Coil, Aluminium Zinc Coil, Floor Plate, Plate, etc), Reinforcing bar

Number of Pages Required

5+ page

Font styles to use
Sans Serif

Requirements
Must have
• Video in the home page showing

```html
<!DOCTYPE html>
<html lang="en">
<head>
<meta charset="utf-8">
<title>KOR Design — Trades in Steel and Iron</title>
<link href="https://fonts.googleapis.com/css2?family=Poppins:ital,wght@0,300;0,400;0,500;0,600;0,700;0,800;1,400&display=swap" rel="stylesheet">
<style>
:root{
  --orange:#f55a00;
  --orange-soft:#f7751f;
  --ink:#111111;
  --text:#555555;
  --navy:#1d2a4d;
  --white:#ffffff;
  --line:#e4e4e4;
  --foot-bar:#f3f3f3;
}
*{box-sizing:border-box;margin:0;padding:0}
html,body{width:1200px;height:3653px;overflow:hidden}
body{font-family:'Poppins',sans-serif;color:var(--ink);background:var(--white);position:relative}
section,header,footer{position:absolute;left:0;width:1200px}
.abs{position:absolute}
.media{position:absolute}
.btn{position:absolute;display:flex;align-items:center;justify-content:center;font-size:12px;font-weight:600;text-transform:uppercase;color:var(--white);background:var(--orange);text-decoration:none}
.btn--outline{background:transparent;border:1.5px solid var(--white)}

/* header */
.site-header{top:0;height:125px;background:var(--white)}
.brand{position:absolute;display:flex;align-items:center;gap:8px;font-weight:700;color:var(--navy)}
.brand__dot{border-radius:50%;background:var(--orange);flex:none}
.site-header .brand{left:92px;top:46px;font-size:22px}
.site-header .brand__dot{width:14px;height:14px}
.nav{position:absolute;top:52px;left:0;font-size:13px;color:#444}
.nav a{position:absolute;white-space:nowrap;color:#444;text-decoration:none}
.nav a.is-active{color:var(--orange)}
.header-divider{position:absolute;left:891px;top:46px;width:1px;height:33px;background:#ddd}
.header-phone{position:absolute;left:922px;top:52px;font-size:12.5px;color:#666;display:flex;align-items:center;gap:8px;white-space:nowrap}
.header-phone strong{color:var(--ink);font-weight:600}

/* hero */
.hero{top:125px;height:442px}
.hero__media{inset:0;background:linear-gradient(100deg,#5b5d60 0%,#2c2e31 35%,#1c1d1f 60%,#3a3029 100%)}
.hero__title-light{position:absolute;right:82px;top:100px;font-size:54px;font-weight:300;color:var(--orange);line-height:1.1}
.hero__title{position:absolute;right:82px;top:165px;font-size:51px;font-weight:800;color:var(--white);line-height:1.1;letter-spacing:-.5px}
.hero__text{position:absolute;right:82px;top:241px;width:420px;text-align:right;font-size:12.5px;line-height:20.5px;color:var(--white)}
.hero__dots{position:absolute;left:1063px;top:336px;display:flex;gap:14px}
.hero__dots span{width:11px;height:11px;border-radius:50%;background:var(--white)}
.hero__dots span.is-current{background:var(--orange)}

/* about */
.about{top:567px;height:450px;background:var(--orange)}
.about h2{position:absolute;left:88px;top:98px;font-size:30px;font-weight:800;color:var(--white)}
.about p{position:absolute;left:88px;top:160px;width:470px;font-size:12.5px;line-height:20.6px;color:var(--white)}
.about .btn{left:88px;top:314px;width:126px;height:44px}
.about__media{left:603px;top:57px;width:489px;height:333px;border-radius:40px;background:radial-gradient(ellipse at 50% 50%,#e9e9ea 0%,#b9babc 45%,rgba(245,90,0,0) 75%)}

/* video + products */
.showcase{top:1017px;height:444px}
.video{position:absolute;left:0;top:0;width:591px;height:444px;background:linear-gradient(135deg,#3a2a18 0%,#6d4a1f 35%,#a9772d 55%,#4a3a2c 80%,#2a2420 100%)}
.video__play{position:absolute;left:234px;top:123px}
.video h3{position:absolute;left:0;width:570px;top:253px;text-align:center;font-size:28px;font-weight:800;color:var(--white)}
.video p{position:absolute;left:145px;width:280px;top:303px;text-align:center;font-size:12.5px;line-height:20.5px;color:var(--white)}
.products{position:absolute;left:591px;top:0;width:609px;height:444px;background:var(--white)}
.products h2{position:absolute;left:97px;top:72px;font-size:28px;font-weight:800}
.product-list{position:absolute;list-style:none;font-size:12.5px;color:#444}
.product-list li{position:absolute;left:0;width:155px;height:41px;padding-top:5px;border-bottom:1px solid var(--line);white-space:nowrap}
.products .btn{left:98px;top:328px;width:127px;height:41px}

/* banner */
.supplier{top:1461px;height:444px}
.supplier__media{inset:0;background:linear-gradient(90deg,#6a6d70 0%,#4b4f52 25%,#2f3235 55%,#1e2022 100%)}
.supplier h2{position:absolute;right:105px;top:95px;text-align:right;font-size:49px;font-weight:800;line-height:63px;color:var(--white);letter-spacing:-.5px}
.supplier p{position:absolute;right:105px;top:254px;width:410px;text-align:right;font-size:12.5px;line-height:20.5px;color:var(--white)}

/* features */
.features{top:1905px;height:1017px;background:var(--white)}
.feature h2{position:absolute;font-size:29px;font-weight:800;line-height:37px}
.feature p{position:absolute;width:400px;font-size:12.5px;line-height:20.5px;color:var(--text)}
.feature .btn{width:125px;height:41px}
.feature__media--sparks{left:590px;top:98px;width:504px;height:420px;background:linear-gradient(135deg,#25384f 0%,#3d5670 40%,#8a95a2 60%,#33485d 100%)}
.feature__media--site{left:88px;top:518px;width:502px;height:418px;background:linear-gradient(180deg,#5c8db5 0%,#a9a3a0 45%,#d38a4c 62%,#1a1a1a 78%,#000 100%)}

/* testimonial */
.testimonial{top:2922px;height:353px;background:var(--orange)}
.testimonial__avatar{position:absolute;left:89px;top:94px;width:146px;height:146px;border-radius:50%;background:linear-gradient(180deg,#dfe6ea 0%,#b9c4cb 100%);border:3px solid var(--white)}
.testimonial__mark{position:absolute;left:290px;top:58px;font-size:48px;font-weight:800;font-style:italic;color:var(--white);line-height:1}
.testimonial blockquote{position:absolute;left:291px;top:117px;width:785px;font-size:12.5px;font-style:italic;line-height:20.6px;color:var(--white)}
.testimonial__name{position:absolute;left:291px;top:220px;font-size:16px;font-weight:600;color:var(--white)}
.testimonial__mail{position:absolute;left:291px;top:243px;font-size:12.5px;color:var(--white)}

/* footer */
.site-footer{top:3275px;height:321px;background:var(--white)}
.site-footer .brand{left:92px;top:127px;font-size:34px}
.site-footer .brand__dot{width:22px;height:22px}
.footer-col h4{position:absolute;font-size:13.5px;font-weight:500;color:var(--ink);white-space:nowrap}
.footer-text{position:absolute;font-size:12px;line-height:20.5px;color:#555;white-space:nowrap}
.footer-text a{color:#555;text-decoration:underline}
.footer-links{position:absolute;list-style:none;font-size:12px;color:#555}
.footer-links li{height:30.8px}
.footer-links li.is-active{color:var(--orange)}
.footer-bar{position:absolute;left:0;top:3596px;width:1200px;height:57px;background:var(--foot-bar)}
.footer-bar p{position:absolute;left:101px;top:20px;font-size:12px;color:#555}
.footer-bar p span{color:var(--orange)}
.socials{position:absolute;left:985px;top:22px;display:flex;gap:26px}
.socials span{width:13px;height:13px;border-radius:50%;background:var(--orange)}
</style>
</head>
<body>

<header class="site-header">
  <div class="brand"><span class="brand__dot"></span>KOR Design</div>
  <nav class="nav">
    <a class="is-active" style="left:492px" href="#">Home</a>
    <a style="left:557px" href="#">About Us</a>
    <a style="left:639px" href="#">Products</a>
    <a style="left:720px" href="#">Reviews</a>
    <a style="left:798px" href="#">Contact</a>
  </nav>
  <div class="header-divider"></div>
  <div class="header-phone">
    <svg width="16" height="16" viewBox="0 0 24 24" fill="none" stroke="#f55a00" stroke-width="2"><path d="M5 3h4l2 5-2.5 1.5a11 11 0 0 0 6 6L16 13l5 2v4a2 2 0 0 1-2 2A16 16 0 0 1 3 5a2 2 0 0 1 2-2z"/></svg>
    <span>Contact us on <strong>123 555 0190</strong></span>
  </div>
</header>

<section class="hero">
  <div class="media hero__media" role="img" aria-label="Stacked steel pipes seen end-on"></div>
  <div class="hero__title-light">Trades in</div>
  <h1 class="hero__title">STEEL AND IRON</h1>
  <p class="hero__text">Industry is Iron and Steel. The company source and supply various steel and metal products within our international network also manage all aspects of the supply process</p>
  <div class="hero__dots"><span class="is-current"></span><span></span><span></span></div>
</section>

<section class="about">
  <h2>ABOUT COMPANY</h2>
  <p>Industry is Iron and Steel. The company source and supply various steel and metal products within our international network also manage all aspects of the supply process from point of manufacture to point of delivery. the goal is to create value within the supply chain by building strong supplier, customers and service providers, funding of both customers and suppliers, experienced risk management, efficient document handling.</p>
  <a class="btn btn--outline" href="#">Learn More</a>
  <div class="media about__media" role="img" aria-label="Group of rolled steel coils"></div>
</section>

<section class="showcase">
  <div class="video" role="img" aria-label="Steel worker cutting metal with sparks flying">
    <svg class="video__play" width="102" height="102" viewBox="0 0 102 102" fill="none" stroke="#fff" stroke-width="2.5"><circle cx="51" cy="51" r="49"/><path d="M40 30 L70 51 L40 72 Z"/></svg>
    <h3>SEE VIDEO</h3>
    <p>The process of how steel is made(or the iron melt, pipe rolled, etc)</p>
  </div>
  <div class="products">
    <h2>OUR PRODUCTS</h2>
    <ul class="product-list" style="left:98px;top:143px">
      <li style="top:0">LSAW pipe</li>
      <li style="top:41px">ERW Pipe</li>
      <li style="top:82px">Steel Coil</li>
      <li style="top:124px;border-bottom:none">Aluminium Zinc Coil</li>
    </ul>
    <ul class="product-list" style="left:324px;top:143px">
      <li style="top:0">Floor Plate</li>
      <li style="top:41px">Reinforcing bar</li>
    </ul>
    <a class="btn" href="#">View More</a>
  </div>
</section>

<section class="supplier">
  <div class="media supplier__media" role="img" aria-label="Construction worker in hard hat among reinforcing bars"></div>
  <h2>BUILDING<br>STRONG SUPPLIER</h2>
  <p>Supply chain by building strong supplier, customers and service providers, funding of both customers and suppliers, experienced risk management, efficient document handling.</p>
</section>

<section class="features">
  <div class="feature">
    <h2 style="left:91px;top:182px">STEEL AND METAL<br>PRODUCTS</h2>
    <p style="left:91px;top:271px">Supply chain by building strong supplier, customers and service providers, funding of both customers and suppliers, experienced risk management, efficient document handling.</p>
    <a class="btn" style="left:89px;top:362px" href="#">Learn More</a>
    <div class="media feature__media--sparks" role="img" aria-label="Worker grinding a steel pipe with sparks"></div>
  </div>
  <div class="feature">
    <div class="media feature__media--site" role="img" aria-label="Construction site silhouette at sunset with crane bucket"></div>
    <h2 style="left:695px;top:599px">CUSTOMERS AND<br>SERVICE PROVIDERS</h2>
    <p style="left:695px;top:687px">Supply chain by building strong supplier, customers and service providers, funding of both customers and suppliers, experienced risk management, efficient document handling.</p>
    <a class="btn" style="left:693px;top:780px" href="#">Learn More</a>
  </div>
</section>

<section class="testimonial">
  <div class="testimonial__avatar" role="img" aria-label="Portrait of a client wearing a hard hat"></div>
  <div class="testimonial__mark">“</div>
  <blockquote>Industry is Iron and Steel. The company source and supply various steel and metal products within our international network also manage all aspects of the supply process from point of manufacture to point of delivery. the goal is to create value within the supply chain by building strong supplier, customers and service providers, funding of both customers and suppliers, experienced risk management, efficient document handling.</blockquote>
  <div class="testimonial__name">Dale Maren</div>
  <div class="testimonial__mail">dale@korsteel.example</div>
</section>

<footer class="site-footer">
  <div class="brand"><span class="brand__dot"></span>KOR Design</div>
  <div class="footer-col">
    <h4 style="left:411px;top:72px">Our Location</h4>
    <svg class="abs" style="left:414px;top:122px" width="18" height="20" viewBox="0 0 24 26" fill="none" stroke="#f55a00" stroke-width="2"><path d="M12 24s8-8 8-14a8 8 0 0 0-16 0c0 6 8 14 8 14z"/><circle cx="12" cy="10" r="3"/></svg>
    <p class="footer-text" style="left:447px;top:122px">Our offices are situated in<br>Australian Territory<br>Harwood, Eastvale.</p>
    <p class="footer-text" style="left:447px;top:204px">For directions <a href="#">click here.</a></p>
  </div>
  <div class="footer-col">
    <h4 style="left:718px;top:72px">Contact Details</h4>
    <svg class="abs" style="left:714px;top:123px" width="18" height="18" viewBox="0 0 24 24" fill="none" stroke="#f55a00" stroke-width="2"><path d="M5 3h4l2 5-2.5 1.5a11 11 0 0 0 6 6L16 13l5 2v4a2 2 0 0 1-2 2A16 16 0 0 1 3 5a2 2 0 0 1 2-2z"/></svg>
    <p class="footer-text" style="left:749px;top:122px">123 555 0190</p>
    <svg class="abs" style="left:714px;top:149px" width="20" height="15" viewBox="0 0 24 18" fill="none" stroke="#f55a00" stroke-width="2"><rect x="1" y="1" width="22" height="16"/><path d="M1 1l11 9 11-9"/></svg>
    <p class="footer-text" style="left:749px;top:146px">info@korsteel.example</p>
  </div>
  <div class="footer-col">
    <h4 style="left:993px;top:72px">Quick Links</h4>
    <ul class="footer-links" style="left:995px;top:122px">
      <li class="is-active">Home</li>
      <li>About Us</li>
      <li>Products</li>
      <li>Reviews</li>
      <li>Contact</li>
    </ul>
  </div>
</footer>

<div class="footer-bar">
  <p>Copyright © 2020 <span>Koral Steel Traders PTY LTD.</span> All rights reserved.</p>
  <div class="socials"><span></span><span></span><span></span><span></span></div>
</div>

</body>
</html>
```